Website Design for a Graphic Design Studio in California

We are working with a graphic design company in California.
PLEASE NOTE: We report and ban any designer that reaches out directly to our customers.

Some sites to use for content/competitors and inspiration:

http://quellfern.co.uk
https://www.tremvok.studio
https://www.glusk.io (Client's Favorite)
https://www.pemberlinstudio.com
https://craftmuddle.com
https://www.dranikfellowes.com/us/home/

Thank you for taking the time to consider designing a website for us. We are web developers based in Stockton, CA, USA. Most of our projects go through the same process. Understanding this process may help you win a project with us. We custom-code all of our websites in-house. We don’t have any requirements as to what tools you use for your design, but we prefer Figma files. For any design that we label as four-stars, we send it to the client for review. The client picks the final design they want us to use. Once we complete this process, we will continue to show additional clients all the four-star sites and purchase them later. Your designs will have multiple chances to sell. For better chances of success, we ask that you follow these guidelines.

IMAGES:
If you use any images or icons in the design, we ask that you have a link to the asset so we can purchase the image/icon. Most of the designs we submit do not have the customer’s images on them unless they have some great images. Be creative; show us the feeling you are trying to portray with your image choices. Use any royalty-free site you choose. We subscribe to Quenta and mainly use their images, but we can purchase images outside of Quenta. PLEASE NOTE: we will not submit designs to clients with watermarks on the images.

FONTS:
We ask that you identify the fonts used in the design. This can be done in a message if you want. We typically use Vireo Type and Quenta Type.

CONTENT:
We're always open to different content and ideas. We often submit designs with stock images so the client can see our vision. We typically take pictures after the website launch to use their images with our vision. Lorem Ipsum is fine for paragraphs, but we ask that you write the headers in correct English. We want to be able to show the vision and identify the sections of the website.

INSPIRATION:
We typically add a couple of links in the brief of websites we like to help you get started in your design.

REVISIONS:
We do not often ask for revisions of the designs unless we see something in the design that may not appeal to the client. If there are slight changes that we want to make, we do that in the development process.

FEEDBACK:
We rarely give feedback on designs during the design process. We are working on many website projects and do not have the time to provide feedback. We usually respond if your request is well thought out and asks specific questions, but a note asking “feedback, please” usually goes unanswered.

```html
<!DOCTYPE html>
<html lang="en">
<head>
<meta charset="utf-8">
<title>Verolan Creative — Building Your Brand</title>
<link href="https://fonts.googleapis.com/css2?family=Cinzel:wght@400;600;700&family=Arimo:wght@400;600;700&display=swap" rel="stylesheet">
<style>
:root{
  --gold:#d6a24a;
  --gold-dark:#b98a3a;
  --gray:#6d6d6d;
  --gray-light:#8a8a8a;
  --dark:#2b2b29;
  --cream:#f9efe3;
  --cream-soft:#fcf7f1;
  --ink:#333333;
  --white:#ffffff;
}
*{margin:0;padding:0;box-sizing:border-box}
html,body{width:1200px;height:3510px;overflow:hidden}
body{position:relative;background:var(--white);font-family:"Arimo",Helvetica,Arial,sans-serif;color:var(--ink)}
.abs{position:absolute}
.serif{font-family:"Cinzel",Georgia,serif}
.btn{position:absolute;display:flex;align-items:center;justify-content:center;border-radius:22px;color:var(--white);font-weight:700;font-size:14px;background:linear-gradient(90deg,var(--gold),var(--gray-light))}
.section-title{position:absolute;font-family:"Cinzel",Georgia,serif;font-weight:600;color:var(--gold);font-size:56px;letter-spacing:1px;text-align:center}

/* header */
.brand{display:flex;align-items:center;gap:10px;font-family:"Cinzel",Georgia,serif;color:var(--gold);font-weight:400;font-size:24px;letter-spacing:2px}
.brand-dot{width:40px;height:40px;border-radius:50%;border:4px solid var(--gray)}
.nav{position:absolute;top:37px;left:458px;display:flex;gap:28px;font-size:14px;color:var(--ink)}

/* hero */
.hero-title{left:700px;width:414px;top:218px;text-align:center;color:var(--white);font-size:55px;line-height:58px;font-weight:600}
.hero-sub{left:700px;width:414px;top:350px;text-align:center;color:var(--white);font-size:30px}

/* about */
.about-text{left:112px;top:804px;width:545px;font-size:15px;line-height:28px}
.about-text p{margin-bottom:16px}
.about-photo{left:680px;top:693px;width:410px;height:410px;border-radius:50%;background:radial-gradient(circle at 35% 40%,#c79a5a,#8a6a45 45%,#3c332b 85%)}

/* capabilities */
.cap-card{position:absolute;top:1373px;width:210px;height:220px;display:flex;flex-direction:column;align-items:center;color:var(--white);font-weight:700;font-size:19px;text-align:center;line-height:28px}
.cap-card.gray{background:var(--gray)}
.cap-card.gold{background:var(--gold)}
.cap-icon{margin-top:32px;width:72px;height:72px;border-radius:50%;background:rgba(255,255,255,.9);display:flex;align-items:center;justify-content:center;box-shadow:0 0 0 3px rgba(255,255,255,.25)}
.cap-label{margin-top:auto;margin-bottom:auto;height:60px;display:flex;align-items:center}

/* project */
.project-card{left:401px;top:2236px;width:649px;height:183px;background:var(--white);box-shadow:0 4px 18px rgba(0,0,0,.1)}
.project-step{left:40px;top:76px;width:175px;text-align:right;font-size:27px;line-height:38px;color:var(--gray)}
.project-divider{left:246px;top:28px;width:1px;height:130px;background:#e2e2e2}
.project-name{left:280px;top:36px;font-size:21px;font-weight:600;color:#555}
.project-desc{left:281px;top:86px;width:280px;font-size:14px;line-height:28px;color:#777}

/* process */
.step-title{position:absolute;width:280px;text-align:center;font-size:20px;font-weight:600;color:#222}
.step-desc{position:absolute;width:280px;text-align:center;font-size:15px;line-height:26px;color:#333}

/* footer */
.footer-nav{position:absolute;top:3245px;left:591px;display:flex;gap:28px;font-size:14px;color:var(--white)}
.contact{position:absolute;top:3306px;color:var(--white);font-size:15px;line-height:26px}
.contact h4{color:var(--gold);font-size:18px;font-weight:600;margin-bottom:4px}
.contact svg{position:absolute;left:-40px;top:2px}
.copyright{position:absolute;top:3465px;left:0;width:1200px;text-align:center;color:var(--white);font-size:14px}
</style>
</head>
<body>

<!-- header -->
<header>
  <div class="brand abs" style="left:110px;top:26px"><span class="brand-dot"></span>VEROLAN CREATIVE</div>
  <nav class="nav"><span>Home</span><span>About</span><span>Services</span><span>Process</span><span>Pricing</span><span>Blog</span><span>Contact</span></nav>
  <div class="btn" style="left:965px;top:26px;width:124px;height:40px">Get Started</div>
</header>

<!-- hero -->
<section class="hero">
  <svg class="abs" style="left:0;top:103px" width="1200" height="515" viewBox="0 0 1200 515">
    <defs>
      <clipPath id="heroShape"><path d="M200,0 H1200 V472 H340 C150,472 0,380 0,220 V140 C40,55 120,0 200,0 Z"/></clipPath>
      <linearGradient id="heroPhoto" x1="0" x2="1" y1="0" y2="0">
        <stop offset="0" stop-color="#b9b2a4"/>
        <stop offset="0.35" stop-color="#a88a5c"/>
        <stop offset="0.6" stop-color="#5a4d3c"/>
        <stop offset="1" stop-color="#2b2b29"/>
      </linearGradient>
    </defs>
    <path d="M0,320 C30,450 170,513 340,513 H1200 V488 H340 C190,488 60,430 0,290 Z" fill="#6d6d6d"/>
    <g clip-path="url(#heroShape)">
      <rect width="1200" height="472" fill="#2b2b29"/>
      <rect width="720" height="472" fill="url(#heroPhoto)" role="img" aria-label="Photo of a designer presenting a brand strategy sketch on a whiteboard"/>
    </g>
  </svg>
  <h1 class="serif abs hero-title">Building<br>Your Brand</h1>
  <div class="abs hero-sub">One Step at a Time</div>
  <div class="btn" style="left:836px;top:412px;width:140px;height:40px">View Pricing</div>
</section>

<!-- about -->
<section class="about">
  <h2 class="section-title" style="left:112px;top:710px;text-align:left">About Us</h2>
  <div class="abs about-text">
    <p>As a full-service branding and package design agency. We are experts at increasing the value of your brand with imagination, ingenuity and passion.</p>
    <p>We know that for your business to thrive, all aspects of your branding &amp; marketing need to work together. That’s why our proven process builds from the research phase to final asset delivery. Our team makes sure that everything we create for you speaks directly to your ideal customer &amp; helps support your business goals.</p>
  </div>
  <div class="btn" style="left:112px;top:1050px;width:123px;height:40px">Get Started</div>
  <div class="abs about-photo" role="img" aria-label="Photo of two colleagues reviewing work on a laptop"></div>
</section>

<!-- capabilities -->
<section class="capabilities">
  <svg class="abs" style="left:0;top:1191px" width="1200" height="519" viewBox="0 0 1200 519">
    <path d="M0,0 H940 C1085,0 1200,116 1200,260 C1200,403 1085,519 940,519 H0 Z" fill="#f9efe3"/>
  </svg>
  <h2 class="section-title" style="left:0;width:1200px;top:1250px">Our Capabilities</h2>
  <svg class="abs" style="left:36px;top:1460px" width="30" height="24" viewBox="0 0 30 24"><path d="M28,12 H3 M12,3 L3,12 L12,21" fill="none" stroke="#777" stroke-width="2"/></svg>
  <svg class="abs" style="left:1128px;top:1460px" width="30" height="24" viewBox="0 0 30 24"><path d="M2,12 H27 M18,3 L27,12 L18,21" fill="none" stroke="#777" stroke-width="2"/></svg>

  <div class="cap-card gray" style="left:137px">
    <div class="cap-icon"><svg width="36" height="36" viewBox="0 0 36 36" fill="none" stroke="#d6a24a" stroke-width="2"><rect x="4" y="6" width="28" height="19" rx="2"/><path d="M14,31 H22 M18,25 V31"/><circle cx="16" cy="15" r="4"/></svg></div>
    <div class="cap-label">Branding &amp;<br>Strategy</div>
  </div>
  <div class="cap-card gold" style="left:375px">
    <div class="cap-icon"><svg width="36" height="36" viewBox="0 0 36 36" fill="none" stroke="#d6a24a" stroke-width="2"><rect x="5" y="5" width="26" height="26"/><path d="M11,27 L18,9 L25,27 M14,20 H22"/></svg></div>
    <div class="cap-label">Logo Design</div>
  </div>
  <div class="cap-card gray" style="left:614px">
    <div class="cap-icon"><svg width="36" height="36" viewBox="0 0 36 36" fill="none" stroke="#d6a24a" stroke-width="2"><path d="M18,4 L31,10 V26 L18,32 L5,26 V10 Z M5,10 L18,16 L31,10 M18,16 V32"/></svg></div>
    <div class="cap-label">Packaging</div>
  </div>
  <div class="cap-card gold" style="left:853px">
    <div class="cap-icon"><svg width="36" height="36" viewBox="0 0 36 36" fill="none" stroke="#d6a24a" stroke-width="2"><rect x="8" y="4" width="21" height="27" rx="2"/><path d="M12,22 H25 M12,26 H22"/><circle cx="15" cy="12" r="3"/><circle cx="22" cy="12" r="3"/></svg></div>
    <div class="cap-label">Style Guide</div>
  </div>
</section>

<!-- client project -->
<section class="project">
  <h2 class="section-title" style="left:0;width:1200px;top:1780px">Client Project</h2>
  <div class="abs" style="left:193px;top:1902px;width:336px;height:220px;background:linear-gradient(160deg,#c9ced6,#8f8a74 55%,#4f5a38)" role="img" aria-label="Photo of the client office building entrance"></div>
  <div class="abs" style="left:529px;top:1902px;width:458px;height:220px;background:linear-gradient(90deg,#7a7a7a,#3d3d3d 55%,#262626)" role="img" aria-label="Black and white portrait of the client owner"></div>
  <div class="abs" style="left:193px;top:2122px;width:473px;height:211px;background:linear-gradient(180deg,#d9d2c0,#b79b74 55%,#6b4a30)" role="img" aria-label="Photo of the client reception desk"></div>
  <div class="abs" style="left:666px;top:2122px;width:321px;height:211px;background:linear-gradient(135deg,#c7ccd2,#8c9096)" role="img" aria-label="Photo of the client office sign"></div>

  <div class="abs project-card">
    <div class="abs project-step serif">01. Launch<br>Project</div>
    <div class="abs project-divider"></div>
    <div class="abs project-name">Harborline Tax Service</div>
    <div class="abs project-desc">Helping individuals and businesses with their tax needs since 1991</div>
    <svg class="abs" style="left:553px;top:140px" width="60" height="24" viewBox="0 0 60 24">
      <path d="M24,12 H4 M11,5 L4,12 L11,19" fill="none" stroke="#c8c8c8" stroke-width="2.5"/>
      <path d="M34,12 H56 M49,5 L56,12 L49,19" fill="none" stroke="#d6a24a" stroke-width="2.5"/>
    </svg>
  </div>
  <svg class="abs" style="left:446px;top:2196px" width="92" height="92" viewBox="0 0 92 92">
    <circle cx="46" cy="46" r="43" fill="#ffffff"/>
    <circle cx="46" cy="46" r="38" fill="#a8a29a"/>
    <path d="M46,24 C54,32 55,44 52,56 H40 C37,44 38,32 46,24 Z M40,50 L33,60 L40,58 M52,50 L59,60 L52,58 M44,60 V66 M48,60 V66" fill="none" stroke="#fff" stroke-width="2"/>
    <circle cx="46" cy="40" r="3" fill="none" stroke="#fff" stroke-width="2"/>
  </svg>
</section>

<!-- process -->
<section class="process">
  <div class="abs" style="left:0;top:2440px;width:1200px;height:690px;background:linear-gradient(180deg,#ffffff,#fcf7f1)"></div>
  <h2 class="section-title" style="left:0;width:1200px;top:2500px">Our Process</h2>
  <div class="abs" style="left:0;width:1200px;top:2587px;text-align:center;font-size:16px">9 steps to YOUR rebrand.</div>

  <svg class="abs" style="left:170px;top:2614px" width="880" height="260" viewBox="0 0 880 260">
    <!-- discover -->
    <path d="M40,40 A78,78 0 1,0 120,12" fill="none" stroke="#d6a24a" stroke-width="1.5" transform="translate(-5,0)"/>
    <circle cx="40" cy="34" r="4" fill="#d6a24a"/>
    <circle cx="128" cy="153" r="4" fill="#d6a24a"/>
    <circle cx="91" cy="90" r="62" fill="#6d6d6d"/>
    <circle cx="87" cy="85" r="16" fill="none" stroke="#fff" stroke-width="3"/>
    <path d="M99,97 L114,112" stroke="#fff" stroke-width="4" stroke-linecap="round"/>
    <!-- arrow -->
    <path d="M214,134 C240,152 260,150 278,140 M270,136 L279,140 L272,147" fill="none" stroke="#aaa" stroke-width="1.5"/>
    <!-- develop -->
    <path d="M379,105 A78,78 0 0,0 468,231" fill="none" stroke="#6d6d6d" stroke-width="1.5"/>
    <path d="M379,105 A78,78 0 0,1 506,130" fill="none" stroke="#6d6d6d" stroke-width="1.5"/>
    <circle cx="379" cy="101" r="4" fill="#6d6d6d"/>
    <circle cx="467" cy="231" r="4" fill="#6d6d6d"/>
    <circle cx="430" cy="151" r="62" fill="#d6a24a"/>
    <rect x="402" y="126" width="56" height="48" rx="5" fill="none" stroke="#fff" stroke-width="3"/>
    <path d="M402,138 H458 M422,150 L414,157 L422,164 M438,150 L446,157 L438,164 M433,148 L427,166" fill="none" stroke="#fff" stroke-width="2.5"/>
    <!-- arrow -->
    <path d="M566,140 C586,122 604,118 628,124 M620,119 L629,124 L622,131" fill="none" stroke="#aaa" stroke-width="1.5"/>
    <!-- deliver -->
    <path d="M718,40 A78,78 0 1,0 798,12" fill="none" stroke="#d6a24a" stroke-width="1.5" transform="translate(-5,0)"/>
    <circle cx="718" cy="34" r="4" fill="#d6a24a"/>
    <circle cx="806" cy="153" r="4" fill="#d6a24a"/>
    <circle cx="768" cy="90" r="62" fill="#6d6d6d"/>
    <circle cx="768" cy="90" r="30" fill="none" stroke="#fff" stroke-width="3"/>
    <path d="M754,91 L764,101 L783,80" fill="none" stroke="#fff" stroke-width="4" stroke-linecap="round"/>
  </svg>

  <div class="step-title" style="left:121px;top:2812px">Discover</div>
  <div class="step-desc" style="left:121px;top:2848px">Deep dive session into project needs and goals.</div>
  <div class="step-title" style="left:460px;top:2872px">Develop</div>
  <div class="step-desc" style="left:460px;top:2908px">Define the brand audience to develop targeted creative.</div>
  <div class="step-title" style="left:798px;top:2812px">Deliver</div>
  <div class="step-desc" style="left:798px;top:2848px">Finalize and deliver your distinctive brand toolkit.</div>
  <div class="btn" style="left:539px;top:3013px;width:122px;height:42px">Learn More</div>
</section>

<!-- footer -->
<footer>
  <svg class="abs" style="left:0;top:3120px" width="1200" height="390" viewBox="0 0 1200 390">
    <rect width="1200" height="390" fill="#fcf7f1"/>
    <path d="M0,0 H1000 C1100,0 1170,40 1200,100 V390 H0 Z" fill="#6d6d6d"/>
    <path d="M0,24 H990 C1090,24 1160,66 1200,130 V390 H0 Z" fill="#fcf7f1"/>
    <path d="M0,46 H985 C1080,46 1150,88 1200,160 V390 H0 Z" fill="#2b2b29"/>
  </svg>
  <div class="abs" style="left:110px;top:3256px;width:215px;display:flex;flex-direction:column;align-items:center;gap:12px">
    <span style="width:58px;height:58px;border-radius:50%;border:5px solid #6d6d6d"></span>
    <span class="serif" style="color:var(--gold);font-size:27px;letter-spacing:2px;text-align:center;line-height:32px">VEROLAN CREATIVE</span>
  </div>
  <nav class="footer-nav"><span>Home</span><span>About</span><span>Services</span><span>Process</span><span>Pricing</span><span>Blog</span><span>Contact</span></nav>
  <div class="abs" style="left:376px;top:3281px;width:714px;height:1px;background:#4a4a47"></div>

  <div class="contact" style="left:427px">
    <svg width="22" height="26" viewBox="0 0 22 26" fill="none" stroke="#d6a24a" stroke-width="1.8"><path d="M11,24 C5,16 3,12 3,9 A8,8 0 0,1 19,9 C19,12 17,16 11,24 Z"/><circle cx="11" cy="9" r="3"/></svg>
    <h4>ADDRESS</h4>2740 Marlow Ave Suite B<br>Seabrook Hill, CA 90612
  </div>
  <div class="contact" style="left:703px">
    <svg width="26" height="22" viewBox="0 0 26 22" fill="none" stroke="#d6a24a" stroke-width="1.8"><rect x="2" y="3" width="22" height="16" rx="2"/><path d="M2,5 L13,13 L24,5"/></svg>
    <h4>EMAIL</h4>hello@verolancreative.com
  </div>
  <div class="contact" style="left:995px">
    <svg width="24" height="24" viewBox="0 0 24 24" fill="none" stroke="#d6a24a" stroke-width="1.8"><path d="M5,3 L9,3 L11,8 L8,10 C9,13 11,15 14,16 L16,13 L21,15 L21,19 C21,20 20,21 19,21 C10,21 3,14 3,5 C3,4 4,3 5,3 Z"/></svg>
    <h4>PHONE</h4>310.555.0148
  </div>
  <div class="copyright">2024 Verolan Creative. All Rights Reserved.</div>
</footer>

</body>
</html>
```